URGENT Christmas Greeting Card for IT Company

We URGENTLY need a Christmas Card for our clients. We are an IT Company that resell softwares from developers. We need the final design for Friday at the latest.

We are looking for a creative, yet elegant christmas card to give to our clients along with a gift. Please use our logo and the same color scheme.

Industry/Entity Type

It Company

Requirements
Must have
• Must have the logo and the colors of christmas and the company.
Nice to have
• I would like to see creative yet elegant designs, its a christmas card that a company is giving to its clients. It would be nice to see a modern, serious and elegant designs.

```html
<!DOCTYPE html>
<html lang="en">
<head>
<meta charset="utf-8">
<title>Christmas Greeting Card – Trellavix</title>
<link href="https://fonts.googleapis.com/css2?family=Cormorant+SC:wght@500&family=Montserrat:wght@600;800&display=swap" rel="stylesheet">
<style>
  :root {
    --page-bg: #e9e9ea;
    --sky-top: #6f93c4;
    --sky-mid: #b9cde6;
    --ridge: #6d7a8e;
    --snow: #f4f6fa;
    --snow-shade: #dfe5ee;
    --greeting: #ffffff;
    --brand-ink: #333336;
    --brand-accent: #e1462c;
    --tagline: #8a1f1a;
  }
  * { margin: 0; padding: 0; box-sizing: border-box; }
  html, body {
    width: 1200px;
    height: 869px;
    overflow: hidden;
    background: var(--page-bg);
  }
  .card {
    position: absolute;
    left: 40px;
    top: 73px;
    width: 1120px;
    height: 722px;
    overflow: hidden;
    box-shadow: 0 10px 30px rgba(0,0,0,0.18);
  }
  .card__scene {
    position: absolute;
    inset: 0;
    background:
      linear-gradient(168deg, transparent 52%, var(--snow-shade) 53%, var(--snow) 70%),
      linear-gradient(180deg, var(--sky-top) 0%, var(--sky-mid) 28%, var(--ridge) 42%, #aab4c4 50%, var(--snow-shade) 62%, var(--snow) 100%);
  }
  .greeting-block { font-size: 0; }
  .greeting {
    position: absolute;
    left: 0;
    width: 100%;
    text-align: center;
    font-family: "Cormorant SC", "Times New Roman", serif;
    font-weight: 500;
    color: var(--greeting);
    line-height: 1;
    white-space: nowrap;
    text-shadow: 0 2px 8px rgba(40,60,90,0.25);
  }
  .greeting--merry {
    top: 50px;
    font-size: 370px;
    letter-spacing: 2px;
    transform: scaleX(0.66);
  }
  .greeting--christmas {
    top: 342px;
    font-size: 227px;
    letter-spacing: 1px;
    transform: scaleX(0.7);
  }
  .brand {
    position: absolute;
    left: 244px;
    top: 553px;
    display: flex;
    align-items: center;
    gap: 22px;
  }
  .brand__mark {
    width: 112px;
    height: 112px;
    border-radius: 50%;
    background: var(--brand-accent);
    flex: none;
  }
  .brand__text {
    display: flex;
    flex-direction: column;
    font-family: "Montserrat", Arial, sans-serif;
  }
  .brand__name {
    font-weight: 800;
    font-size: 56px;
    line-height: 1;
    color: var(--brand-ink);
    white-space: nowrap;
  }
  .brand__tagline {
    margin-top: 8px;
    font-weight: 600;
    font-size: 22px;
    letter-spacing: 0.3px;
    color: var(--tagline);
    white-space: nowrap;
  }
</style>
</head>
<body>
  <main class="card">
    <div class="card__scene" role="img" aria-label="Photograph of snow-covered alpine mountains under a blue winter sky"></div>
    <h1 class="greeting-block">
      <span class="greeting greeting--merry">Merry</span>
      <span class="greeting greeting--christmas">Christmas</span>
    </h1>
    <div class="brand">
      <div class="brand__mark"></div>
      <div class="brand__text">
        <span class="brand__name">TRELLAVIX</span>
        <span class="brand__tagline">IT CONSULTING AND SERVICES</span>
      </div>
    </div>
  </main>
</body>
</html>
```